Women's Health Company needs business card

We need a business card for a USA based women's health care company. We use digital technology to enhance therapy prescribed by clinicians for their patients

```html
<!DOCTYPE html>
<html lang="en">
<head>
<meta charset="utf-8">
<title>Lumora Health — Business Card</title>
<link rel="stylesheet" href="https://fonts.googleapis.com/css2?family=Montserrat:wght@400;500;600&display=swap">
<style>
  :root {
    --bg: #0c0c0c;
    --card: #1c1c1c;
    --card-edge: #262626;
    --silver: #cfcfcf;
    --silver-soft: #a9a9a9;
    --rule: #8a8a8a;
  }
  * { box-sizing: border-box; margin: 0; padding: 0; }
  html, body {
    width: 1200px; height: 900px; overflow: hidden;
    background: var(--bg);
    font-family: 'Montserrat', sans-serif;
    color: var(--silver);
  }
  .stage {
    width: 1200px; height: 900px;
    display: flex; flex-direction: column;
    align-items: center; justify-content: center; gap: 44px;
  }
  .card {
    width: 700px; height: 400px;
    background: linear-gradient(135deg, var(--card) 0%, #222 55%, var(--card) 100%);
    border: 1px solid var(--card-edge);
    box-shadow: 0 18px 40px rgba(0,0,0,.6);
    position: relative;
    display: flex; align-items: center;
  }
  .card--front { justify-content: center; }
  .brand {
    display: flex; align-items: center; gap: 14px;
  }
  .brand__dot {
    width: 14px; height: 14px; border-radius: 50%;
    background: var(--silver);
  }
  .brand__name {
    font-size: 44px; font-weight: 500; letter-spacing: 1px;
    color: var(--silver);
  }
  .card--back { padding: 0 0 0 60px; }
  .card--back .brand__name { font-size: 36px; }
  .divider {
    width: 1px; height: 220px; background: var(--rule);
    margin: 0 36px 0 34px;
  }
  .contact { display: flex; flex-direction: column; }
  .contact__name {
    font-size: 22px; font-weight: 600; letter-spacing: 1px;
    text-transform: uppercase; color: var(--silver);
  }
  .contact__role {
    font-size: 14px; color: var(--silver-soft); margin-bottom: 16px;
  }
  .contact__address {
    font-size: 16px; line-height: 1.35; color: var(--silver-soft);
    margin-bottom: 12px;
  }
  .contact__line {
    display: flex; align-items: center; gap: 8px;
    font-size: 16px; line-height: 1.6; color: var(--silver);
  }
  .contact__icon { width: 13px; height: 13px; flex: none; }
</style>
</head>
<body>
<main class="stage">
  <section class="card card--front">
    <div class="brand">
      <span class="brand__dot"></span>
      <span class="brand__name">Lumora Health</span>
    </div>
  </section>

  <section class="card card--back">
    <div class="brand">
      <span class="brand__dot"></span>
      <span class="brand__name">Lumora Health</span>
    </div>
    <div class="divider"></div>
    <div class="contact">
      <p class="contact__name">Daniel Reyes</p>
      <p class="contact__role">Director</p>
      <p class="contact__address">1175 Alder Lane<br>Rochester, NY 14604</p>
      <p class="contact__line">
        <svg class="contact__icon" viewBox="0 0 16 16" aria-hidden="true"><path fill="#cfcfcf" d="M3.6 1.2l2.2 2.6-1.3 1.8c.9 2 2.7 3.8 4.8 4.8l1.8-1.3 2.6 2.2-1.4 2.4C7 13.6 2.4 9 1.2 3z"/></svg>
        585.555.0182
      </p>
      <p class="contact__line">
        <svg class="contact__icon" viewBox="0 0 16 16" aria-hidden="true"><rect x="1.5" y="3.5" width="13" height="9" fill="none" stroke="#cfcfcf" stroke-width="1.4"/><path d="M1.5 3.5L8 9l6.5-5.5" fill="none" stroke="#cfcfcf" stroke-width="1.4"/></svg>
        hello@lumorahealth.com
      </p>
      <p class="contact__line">
        <svg class="contact__icon" viewBox="0 0 16 16" aria-hidden="true"><g fill="none" stroke="#cfcfcf" stroke-width="1.3"><circle cx="8" cy="8" r="6.3"/><ellipse cx="8" cy="8" rx="2.8" ry="6.3"/><path d="M1.7 8h12.6"/></g></svg>
        www.lumorahealth.com
      </p>
    </div>
  </section>
</main>
</body>
</html>
```